An innovative software company needs a business card!

We need a business card design for our new innovative software company. Please use the details for the business card provided in business card details section. We will use the business card paper like: https://www.prindlecard.example/us/products/nfc/business-cards-plus.html Our company name: celvane We have already a logo and colors to use in business cards too ,

Target Market(s)

App & Sofware Development

Industry/Entity Type

Software

Contact Information for Business Card

Lukas Brenner, BSc.
Owner and Creative Superhero

Adress:
Pelzerweg 14/3/1708
A - 1100, Wien

Tel: +43 (0) 664 219 53 08
Email: lukas.brenner@celvane.example
Web: www.celvane.example

Requirements
Must have
• - Use our logo
Nice to have
• It would be nice to have a nice picture on the backside. (About apps, software, technicals or funy stuff) - Use our colors as in business card (optional)

```html
<!DOCTYPE html>
<html lang="en">
<head>
<meta charset="utf-8">
<title>celvane business card</title>
<link rel="stylesheet" href="https://fonts.googleapis.com/css2?family=Open+Sans:wght@400;600;700&display=swap">
<style>
  :root {
    --cyan: #1fbcd8;
    --grey-pale: #d9d9d9;
    --ink: #1c1c1c;
    --paper: #ffffff;
    --stage: #d6d9dd;
    --back-deep: #0f7f93;
    --back-mid: #25b7c9;
    --back-green: #3fd07a;
    --back-blue: #2a6fd1;
  }
  * { margin: 0; padding: 0; box-sizing: border-box; }
  html, body { width: 1200px; height: 1200px; overflow: hidden; }
  body {
    background: var(--stage);
    font-family: "Open Sans", sans-serif;
    position: relative;
  }
  .card {
    position: absolute;
    left: 180px;
    width: 840px;
    height: 480px;
    overflow: hidden;
    box-shadow: 0 10px 30px rgba(0,0,0,.18);
  }
  /* Back side */
  .card-back { top: 70px; background: var(--back-deep); }
  .back-artwork {
    position: absolute; inset: 0;
    background:
      radial-gradient(ellipse at 62% 20%, rgba(160,255,220,.55), transparent 45%),
      radial-gradient(ellipse at 35% 85%, var(--back-green), transparent 50%),
      radial-gradient(ellipse at 20% 55%, var(--back-blue), transparent 45%),
      linear-gradient(135deg, var(--back-mid), var(--back-deep));
  }
  .back-wordmark {
    position: absolute; right: 40px; top: 30px;
    font-weight: 700; font-size: 110px; line-height: 1;
    color: rgba(8,70,85,.35);
    transform: rotate(180deg);
  }
  /* Front side */
  .card-front { top: 640px; background: var(--paper); }
  .decor-circle {
    position: absolute; left: -150px; top: 210px;
    width: 470px; height: 470px; border-radius: 50%;
    background: var(--grey-pale);
  }
  .logo {
    position: absolute; left: 385px; top: 38px;
    display: flex; align-items: center; gap: 22px;
  }
  .logo-dot {
    width: 92px; height: 92px; border-radius: 50%;
    background: var(--cyan);
  }
  .logo-name {
    font-weight: 700; font-size: 84px; line-height: 1;
    color: var(--cyan); letter-spacing: -1px;
  }
  .rule {
    position: absolute; left: 385px; right: 30px;
    height: 2px; background: var(--cyan);
  }
  .rule-top { top: 168px; }
  .rule-mid { top: 292px; }
  .person { position: absolute; left: 395px; top: 188px; }
  .person-name {
    font-weight: 600; font-size: 38px; color: var(--cyan);
    letter-spacing: -.5px; line-height: 1.2;
  }
  .person-role { font-size: 22px; color: var(--ink); margin-top: 4px; }
  .contacts {
    position: absolute; left: 395px; right: 24px; top: 310px;
    list-style: none; font-size: 20px; color: var(--ink);
  }
  .contacts li { display: flex; align-items: center; gap: 12px; height: 37px; white-space: nowrap; }
  .contacts svg { width: 22px; height: 22px; flex: none; fill: var(--cyan); }
</style>
</head>
<body>

<section class="card card-back">
  <div class="back-artwork" role="img" aria-label="Glowing globe covered in colourful app icons with light rays"></div>
  <div class="back-wordmark">celvane</div>
</section>

<section class="card card-front">
  <div class="decor-circle"></div>

  <div class="logo">
    <span class="logo-dot"></span>
    <span class="logo-name">celvane</span>
  </div>

  <div class="rule rule-top"></div>
  <div class="person">
    <div class="person-name">LUKAS BRENNER</div>
    <div class="person-role">Owner and Creative Superhero</div>
  </div>
  <div class="rule rule-mid"></div>

  <ul class="contacts">
    <li>
      <svg viewBox="0 0 24 24"><path d="M6.6 10.8a15 15 0 0 0 6.6 6.6l2.2-2.2c.3-.3.7-.4 1-.2 1.1.4 2.3.6 3.6.6.6 0 1 .4 1 1V20c0 .6-.4 1-1 1A17 17 0 0 1 3 4c0-.6.4-1 1-1h3.5c.6 0 1 .4 1 1 0 1.3.2 2.5.6 3.6.1.3 0 .7-.2 1z"/></svg>
      +43 (0) 664 219 53 08
    </li>
    <li>
      <svg viewBox="0 0 24 24"><path d="M2 5h20v14H2z M2 5l10 8 10-8" stroke="#fff" stroke-width="1.5"/></svg>
      lukas.brenner@celvane.example
    </li>
    <li>
      <svg viewBox="0 0 24 24"><circle cx="12" cy="12" r="10"/><path d="M2 12h20M12 2c3 3 3 17 0 20M12 2c-3 3-3 17 0 20" stroke="#fff" stroke-width="1.3" fill="none"/></svg>
      www.celvane.example
    </li>
    <li>
      <svg viewBox="0 0 24 24"><path d="M12 3 2 12h3v9h5v-6h4v6h5v-9h3z"/></svg>
      Pelzerweg 14/3/1708, A - 1100 Wien
    </li>
  </ul>
</section>

</body>
</html>
```